Business Card Design - Law Firm

I need a business card design. I have attached a picture of the law firm's website and logo. The business card design should be consistent with those pictures. There should be a place for the employee name, employee job title, telephone number, facsimile number, address, website url, and email address for each employee.
Industry/Entity Type
Business

```html
<!DOCTYPE html>
<html lang="en">
<head>
<meta charset="UTF-8">
<title>Aldermoor Law – Business Card</title>
<link rel="stylesheet" href="https://fonts.googleapis.com/css2?family=Marcellus&family=Gelasio:wght@400&family=Tinos:wght@400;700&display=swap">
<style>
  :root {
    --paper: #ffffff;
    --ink: #2e2e2e;
    --gold: #9d8a45;
    --bar: #353535;
    --rule: #b9b9b9;
    --mark: #1c1c1c;
  }
  html, body {
    margin: 0;
    padding: 0;
    width: 1200px;
    height: 667px;
    overflow: hidden;
    background: var(--paper);
  }
  .card {
    position: relative;
    width: 1200px;
    height: 667px;
    background: var(--paper);
    overflow: hidden;
  }
  .brand {
    position: absolute;
    left: 50px;
    top: 50px;
    display: flex;
    align-items: center;
    gap: 56px;
  }
  .brand-square {
    width: 140px;
    height: 140px;
    background: var(--mark);
  }
  .brand-divider {
    position: absolute;
    left: 214px;
    top: 6px;
    width: 1px;
    height: 170px;
    background: #e2e2e2;
  }
  .brand-name {
    font-family: "Marcellus", serif;
    font-size: 80px;
    font-weight: 400;
    color: var(--gold);
    letter-spacing: 1px;
    margin-left: 30px;
    white-space: nowrap;
  }
  .name-bar {
    position: absolute;
    left: 411px;
    top: 285px;
    width: 789px;
    height: 68px;
    background: var(--bar);
    border-top-left-radius: 14px;
    display: flex;
    align-items: center;
  }
  .person-name {
    font-family: "Gelasio", serif;
    font-size: 52px;
    color: #ffffff;
    letter-spacing: 3px;
    margin-left: 30px;
  }
  .job-title {
    position: absolute;
    right: 20px;
    top: 372px;
    font-family: "Gelasio", serif;
    font-size: 41px;
    color: var(--ink);
    letter-spacing: 3px;
  }
  .divider {
    position: absolute;
    left: 0;
    top: 477px;
    width: 1200px;
    height: 2px;
    background: var(--rule);
  }
  .contact {
    font-family: "Tinos", serif;
    font-size: 31px;
    color: var(--gold);
    position: absolute;
  }
  .contact .label {
    color: #111;
    font-weight: 700;
  }
  .phones { left: 22px; top: 490px; }
  .phones .fax { margin-left: 38px; }
  .email { right: 12px; top: 532px; }
  .web { right: 12px; top: 578px; }
</style>
</head>
<body>
  <div class="card">
    <div class="brand">
      <div class="brand-square"></div>
      <div class="brand-divider"></div>
      <div class="brand-name">Aldermoor Law</div>
    </div>

    <div class="name-bar">
      <span class="person-name">Sam Porter</span>
    </div>
    <div class="job-title">Senior Advocate</div>

    <div class="divider"></div>

    <div class="contact phones">
      <span class="label">Tel:</span> 555.010.234
      <span class="fax"><span class="label">Fax:</span> 555.010.235</span>
    </div>
    <div class="contact email"><span class="label">e-mail:</span> sam.porter@aldermoorlaw.com</div>
    <div class="contact web">www.aldermoorlaw.com</div>
  </div>
</body>
</html>
```